Website, SMS, Chat Translator business

Im very open to the design, idea and card Shape. I just have my Web and business Names. Needs to be in Vector and PDF format Please. Based out of Miami, FL . Giving list of names to see what is the best naming and resonates with the brand. glossaverse-hub.com
linguabrook.com
pagewordshiftlabs.com everyvoicebridge.com. txt-polyglotia.com . rendertonguesco.com pagewordshiftlab.com.
talkmorphers.com

```html
<!DOCTYPE html>
<html lang="en">
<head>
<meta charset="utf-8">
<title>Translator Business Cards</title>
<link rel="stylesheet" href="https://fonts.googleapis.com/css2?family=Poppins:wght@400;500;600;700;800&display=swap">
<style>
  :root {
    --backdrop: #cce3f5;
    --navy: #2a5474;
    --blue: #0a79c6;
    --sky: #22bdfd;
    --charcoal: #4a4a4a;
    --ink: #3a3a3a;
    --mist: #d3eafc;
    --white: #ffffff;
    --photo-deep: #0b4fa8;
    --photo-warm: #3a2a22;
  }
  html, body {
    margin: 0;
    padding: 0;
    width: 1200px;
    height: 720px;
    overflow: hidden;
    background: var(--backdrop);
  }
  .canvas {
    position: relative;
    width: 1200px;
    height: 720px;
    background: var(--backdrop);
    font-family: "Poppins", sans-serif;
  }
  .card {
    position: absolute;
    width: 527px;
    height: 311px;
    display: block;
  }
  .card--front-a { left: 61px;  top: 34px; }
  .card--back-a  { left: 612px; top: 34px; }
  .card--front-b { left: 61px;  top: 369px; }
  .card--back-b  { left: 612px; top: 369px; }
  .card text { font-family: "Poppins", sans-serif; }
  .title-white  { fill: var(--white); font-weight: 800; }
  .title-navy   { fill: var(--navy); font-weight: 800; }
  .name         { fill: var(--charcoal); font-weight: 700; }
  .role-blue    { fill: var(--blue); font-weight: 400; }
  .role-sky     { fill: var(--sky); font-weight: 400; }
  .detail       { fill: var(--charcoal); font-weight: 400; }
  .label        { fill: var(--charcoal); font-weight: 600; }
  .service-light{ fill: var(--white); font-weight: 700; }
  .service-dark { fill: var(--ink); font-weight: 700; }
  .quantity {
    position: absolute;
    right: 22px;
    bottom: 12px;
    margin: 0;
    font-weight: 800;
    font-size: 23px;
    color: var(--ink);
  }
  .icon { fill: none; stroke: var(--white); stroke-width: 2; stroke-linecap: round; stroke-linejoin: round; }
  .icon-solid { fill: var(--white); stroke: none; }
</style>
</head>
<body>
<div class="canvas">

  <svg width="0" height="0" style="position:absolute" aria-hidden="true">
    <defs>
      <symbol id="ico-laptop" viewBox="0 0 24 24">
        <rect class="icon" x="4" y="5" width="16" height="10" rx="1"/>
        <path class="icon" d="M2 18h20"/>
      </symbol>
      <symbol id="ico-mobile" viewBox="0 0 24 24">
        <rect class="icon" x="7" y="2" width="10" height="20" rx="2"/>
        <circle class="icon-solid" cx="12" cy="18" r="1.2"/>
      </symbol>
      <symbol id="ico-chat" viewBox="0 0 24 24">
        <path class="icon-solid" d="M10 3c-4.4 0-8 2.7-8 6 0 1.7.9 3.2 2.4 4.3L3.5 17l4-2c.8.2 1.6.3 2.5.3 4.4 0 8-2.7 8-6s-3.6-6-8-6z"/>
        <path class="icon-solid" d="M19.5 9.5c.1.4.1.8.1 1.2 0 3.8-4 6.8-8.9 6.9 1.2 1.3 3.2 2.1 5.3 2.1.6 0 1.2-.1 1.8-.2l3.2 1.5-.7-2.8c1.1-.9 1.7-2 1.7-3.3 0-2.1-1-4-2.5-5.4z"/>
      </symbol>
      <symbol id="ico-pin" viewBox="0 0 24 24">
        <path class="icon-solid" d="M12 2a7 7 0 0 0-7 7c0 5.2 7 13 7 13s7-7.8 7-13a7 7 0 0 0-7-7zm0 9.5A2.5 2.5 0 1 1 12 6.5a2.5 2.5 0 0 1 0 5z"/>
      </symbol>
      <symbol id="ico-phone" viewBox="0 0 24 24">
        <path class="icon-solid" d="M6.6 10.8a15 15 0 0 0 6.6 6.6l2.2-2.2a1 1 0 0 1 1-.25c1.1.4 2.3.6 3.6.6a1 1 0 0 1 1 1V20a1 1 0 0 1-1 1A17 17 0 0 1 3 4a1 1 0 0 1 1-1h3.5a1 1 0 0 1 1 1c0 1.3.2 2.5.6 3.6a1 1 0 0 1-.25 1z"/>
      </symbol>
      <symbol id="ico-mail" viewBox="0 0 24 24">
        <rect class="icon" x="3" y="6" width="18" height="12" rx="1.5"/>
        <path class="icon" d="M3.5 7l8.5 6 8.5-6"/>
      </symbol>
    </defs>
  </svg>

  <!-- Front, framed edition -->
  <svg class="card card--front-a" viewBox="0 0 1087 641" role="group" aria-label="Translator card front">
    <rect width="1087" height="641" fill="var(--navy)"/>
    <rect x="117" y="40" width="926" height="561" fill="var(--white)"/>
    <rect x="124" y="47" width="912" height="547" fill="var(--mist)"/>
    <polygon points="0,96 660,96 564,246 0,246" fill="var(--blue)"/>
    <polygon points="0,246 564,246 514,320 564,397 0,397" fill="var(--sky)"/>
    <polygon points="0,397 564,397 660,547 0,547" fill="var(--charcoal)"/>
    <text class="title-white" x="34" y="344" font-size="70">TRANSLATOR</text>

    <rect x="666" y="160" width="3" height="322" fill="var(--blue)"/>
    <text class="name" x="685" y="194" font-size="28">MARISOL VANCE</text>
    <text class="role-blue" x="685" y="226" font-size="21">CEO</text>

    <rect x="668" y="262" width="52" height="52" fill="var(--blue)"/>
    <use href="#ico-pin" x="683" y="277" width="22" height="22"/>
    <text class="detail" x="736" y="282" font-size="17">418 Coral Reef Way, Suite 12,</text>
    <text class="detail" x="736" y="307" font-size="17">Miami, FL 33131, United States</text>

    <rect x="668" y="339" width="52" height="52" fill="var(--blue)"/>
    <use href="#ico-phone" x="684" y="355" width="20" height="20"/>
    <text class="detail" x="736" y="359" font-size="17">(+1) 0305 -1842-761</text>
    <text class="detail" x="736" y="384" font-size="17">1-800-555-0148</text>

    <rect x="668" y="415" width="52" height="52" fill="var(--blue)"/>
    <use href="#ico-mail" x="684" y="431" width="20" height="20"/>
    <text class="detail" x="736" y="436" font-size="17">hello@linguabrook.com</text>
    <text class="detail" x="736" y="461" font-size="17">www.linguabrook.com</text>
  </svg>

  <!-- Back, framed edition -->
  <svg class="card card--back-a" viewBox="0 0 1087 641" role="group" aria-label="Translator card back">
    <rect width="1087" height="641" fill="var(--navy)"/>
    <rect x="44" y="40" width="925" height="561" fill="var(--white)"/>
    <rect x="51" y="47" width="911" height="547" fill="var(--mist)"/>
    <text class="title-navy" x="93" y="332" font-size="63">TRANSLATOR</text>

    <polygon points="543,96 1087,96 1087,246 643,246" fill="var(--blue)"/>
    <polygon points="643,246 1087,246 1087,397 643,397 618,320" fill="var(--sky)"/>
    <polygon points="643,397 1087,397 1087,547 543,547" fill="var(--charcoal)"/>

    <circle cx="593" cy="169" r="46" fill="var(--blue)"/>
    <use href="#ico-laptop" x="567" y="143" width="48" height="48"/>
    <text class="service-light" x="663" y="181" font-size="32">WEBSITE TRANSLATOR</text>

    <circle cx="663" cy="320" r="43" fill="var(--sky)"/>
    <use href="#ico-mobile" x="643" y="300" width="40" height="40"/>
    <text class="service-light" x="738" y="332" font-size="32">SMS TRANSLATOR</text>

    <circle cx="593" cy="470" r="46" fill="var(--charcoal)"/>
    <use href="#ico-chat" x="567" y="448" width="46" height="46"/>
    <text class="service-light" x="663" y="482" font-size="32">CHAT TRANSLATOR</text>
  </svg>

  <!-- Front, geometric edition -->
  <svg class="card card--front-b" viewBox="0 0 1087 641" role="group" aria-label="Translator card front, geometric">
    <rect width="1087" height="641" fill="var(--white)"/>
    <path d="M525,0 H1087 V66 L870,272 Q836,304 802,272 Z" fill="var(--sky)"/>
    <path d="M525,641 H1087 V578 L870,376 Q836,344 802,376 Z" fill="var(--blue)"/>
    <path d="M1087,86 V556 L882,350 Q852,320 882,290 Z" fill="var(--charcoal)"/>
    <text class="title-white" x="666" y="107" font-size="50">TRANSLATOR</text>

    <rect x="57" y="66" width="6" height="474" fill="var(--blue)"/>
    <rect x="29" y="93" width="306" height="6" fill="var(--sky)"/>
    <text class="name" x="120" y="158" font-size="42">Marisol Vance</text>
    <text class="role-sky" x="120" y="200" font-size="32">CEO</text>

    <circle cx="60" cy="286" r="31" fill="var(--blue)"/>
    <use href="#ico-pin" x="45" y="271" width="30" height="30"/>
    <text class="label" x="121" y="276" font-size="25">Address:</text>
    <text class="detail" x="121" y="308" font-size="17">2270 Biscayne Bay Road, FL 33137,</text>
    <text class="detail" x="121" y="337" font-size="17">United States</text>

    <circle cx="60" cy="398" r="31" fill="var(--blue)"/>
    <use href="#ico-phone" x="46" y="384" width="28" height="28"/>
    <text class="label" x="121" y="388" font-size="25">Phone:</text>
    <text class="detail" x="121" y="420" font-size="17">(+1) 305 555 – 0192</text>
    <text class="detail" x="121" y="453" font-size="17">1800-5550-27140</text>

    <circle cx="60" cy="520" r="31" fill="var(--blue)"/>
    <use href="#ico-mail" x="45" y="505" width="30" height="30"/>
    <text class="label" x="121" y="510" font-size="25">Email:</text>
    <text class="detail" x="121" y="542" font-size="17">hello@linguabrook.com</text>
    <text class="detail" x="121" y="575" font-size="17">www.linguabrook.com</text>
  </svg>

  <!-- Back, geometric edition -->
  <svg class="card card--back-b" viewBox="0 0 1087 641" role="group" aria-label="Translator card back, geometric">
    <defs>
      <linearGradient id="tone-top" x1="0" y1="0" x2="1" y2="1">
        <stop offset="0" stop-color="#1a6fb8"/>
        <stop offset="1" stop-color="#1fa3e8"/>
      </linearGradient>
      <linearGradient id="tone-side" x1="0" y1="0" x2="0" y2="1">
        <stop offset="0" stop-color="#4a5a3a"/>
        <stop offset="1" stop-color="var(--photo-warm)"/>
      </linearGradient>
      <linearGradient id="tone-bottom" x1="0" y1="0" x2="1" y2="1">
        <stop offset="0" stop-color="#1b7fd6"/>
        <stop offset="1" stop-color="var(--photo-deep)"/>
      </linearGradient>
    </defs>
    <rect width="1087" height="641" fill="var(--white)"/>
    <path d="M0,0 H560 L284,272 Q250,304 216,272 L0,60 Z" fill="url(#tone-top)" role="img" aria-label="Photo: team reviewing a translated website on a screen"/>
    <path d="M0,86 L200,290 Q230,320 200,350 L0,556 Z" fill="url(#tone-side)" role="img" aria-label="Photo: hands typing text messages on a phone"/>
    <path d="M0,641 H560 L284,370 Q250,338 216,370 L0,578 Z" fill="url(#tone-bottom)" role="img" aria-label="Photo: chat bubbles over a person using a smartphone"/>

    <circle cx="588" cy="169" r="45" fill="var(--sky)"/>
    <use href="#ico-laptop" x="564" y="145" width="48" height="48"/>
    <text class="service-dark" x="663" y="181" font-size="32">WEBSITE TRANSLATOR</text>

    <circle cx="448" cy="320" r="45" fill="var(--charcoal)"/>
    <use href="#ico-mobile" x="428" y="300" width="40" height="40"/>
    <text class="service-dark" x="521" y="332" font-size="32">SMS TRANSLATOR</text>

    <circle cx="588" cy="471" r="45" fill="var(--blue)"/>
    <use href="#ico-chat" x="565" y="448" width="46" height="46"/>
    <text class="service-dark" x="663" y="482" font-size="32">CHAT TRANSLATOR</text>
  </svg>

  <p class="quantity">x10</p>
</div>
</body>
</html>
```